BRIARWOOD MEDICAL SERVICES , stationary design

Clean , minimal , modern

Target Market(s)

Healthcare

Font styles to use
Sans Serif
Other font styles liked:
• Sans serif rounded light

Colors
b1b1b1

Requirements
Must have
• Must Have:
• - must have letter head, business card, envelope, fax sheet, id badge, folder, thank you card, notebook, invoice sheet, stamp , received stamp
• Nice to Have:
• - nice to have them all custom made (letterhead,envelope, business card, I’d badge etc
• - you need to change the logo colors , icon to dark blue and logo text to dark grey and another option with dark green icon and dark grey logo text .

```html
<!DOCTYPE html>
<html lang="en">
<head>
<meta charset="utf-8">
<title>Briarwood Medical Services – Business Card</title>
<link rel="stylesheet" href="https://fonts.googleapis.com/css2?family=Roboto:wght@400;500;700&display=swap">
<style>
  :root {
    --navy: #1f2a64;
    --grey-text: #4a4a4a;
    --soft-grey: #b1b1b1;
    --backdrop: #a9a9a9;
    --silver-light: #d6d7d9;
    --silver-dark: #9fa1a4;
    --paper: #ffffff;
  }
  * { margin: 0; padding: 0; box-sizing: border-box; }
  html, body {
    width: 1200px; height: 885px; overflow: hidden;
    background: radial-gradient(ellipse at 50% 40%, #c4c4c4 0%, var(--backdrop) 70%, #8e8e8e 100%);
    font-family: "Roboto", sans-serif;
  }
  .canvas { position: relative; width: 1200px; height: 885px; }

  .card {
    position: absolute; width: 540px; height: 310px; border-radius: 2px;
    box-shadow: 0 14px 30px rgba(0,0,0,.28), 0 2px 4px rgba(0,0,0,.2);
  }

  /* Back side */
  .card-back {
    left: 70px; top: 100px;
    background: linear-gradient(135deg, var(--silver-light) 0%, #c3c4c6 45%, var(--silver-dark) 100%);
    display: flex; flex-direction: column; align-items: center; justify-content: center;
  }
  .back-brand { display: flex; align-items: center; gap: 14px; }
  .back-brand .mark { width: 30px; height: 30px; background: var(--navy); }
  .back-brand .name {
    font-weight: 700; font-size: 46px; color: var(--paper); letter-spacing: 1px;
  }
  .back-url {
    margin-top: 70px; font-size: 13px; color: var(--paper); letter-spacing: 2.4px;
  }

  /* Front side */
  .card-front { left: 590px; top: 470px; background: var(--paper); }
  .brand {
    position: absolute; right: 40px; top: 46px;
    display: flex; align-items: center; gap: 10px;
  }
  .brand .mark { width: 20px; height: 20px; background: var(--navy); }
  .brand .name { font-weight: 700; font-size: 15px; color: var(--navy); letter-spacing: .4px; }

  .holder { position: absolute; left: 36px; top: 58px; }
  .holder .person { font-weight: 700; font-size: 22px; color: var(--navy); }
  .holder .role { font-size: 15px; color: var(--soft-grey); margin-top: 1px; }

  .divider { position: absolute; left: 36px; right: 40px; top: 126px; height: 1px; background: var(--navy); }

  .contacts { position: absolute; left: 36px; top: 148px; list-style: none; }
  .contacts li {
    display: flex; align-items: center; gap: 10px;
    font-size: 15px; color: var(--grey-text); line-height: 22px;
  }
  .contacts svg { width: 14px; height: 14px; fill: var(--navy); flex: none; }

  .address {
    position: absolute; right: 40px; top: 148px; text-align: right;
    font-size: 14px; color: var(--grey-text); line-height: 20px;
  }
</style>
</head>
<body>
<div class="canvas">

  <section class="card card-back" aria-label="Business card back">
    <div class="back-brand">
      <span class="mark"></span>
      <span class="name">BRIARWOOD</span>
    </div>
    <p class="back-url">www.briarwoodmedicalservices.com</p>
  </section>

  <section class="card card-front" aria-label="Business card front">
    <div class="brand">
      <span class="mark"></span>
      <span class="name">BRIARWOOD MEDICAL SERVICES</span>
    </div>

    <div class="holder">
      <p class="person">DANIEL HARPER</p>
      <p class="role">CEO/FOUNDER</p>
    </div>

    <div class="divider"></div>

    <ul class="contacts">
      <li>
        <svg viewBox="0 0 24 24" aria-hidden="true"><path d="M6.6 10.8a15.1 15.1 0 0 0 6.6 6.6l2.2-2.2c.3-.3.7-.4 1-.2 1.1.4 2.3.6 3.6.6.6 0 1 .4 1 1V20c0 .6-.4 1-1 1A17 17 0 0 1 3 4c0-.6.4-1 1-1h3.5c.6 0 1 .4 1 1 0 1.3.2 2.5.6 3.6.1.3 0 .7-.2 1z"/></svg>
        555 218 4730
      </li>
      <li>
        <svg viewBox="0 0 24 24" aria-hidden="true"><path d="M7 1h10a2 2 0 0 1 2 2v18a2 2 0 0 1-2 2H7a2 2 0 0 1-2-2V3a2 2 0 0 1 2-2zm0 3v14h10V4zm5 15.5a1 1 0 1 0 0 2 1 1 0 0 0 0-2z"/></svg>
        555 904 6127
      </li>
      <li>
        <svg viewBox="0 0 24 24" aria-hidden="true"><path d="M7 2h10v5H7zM4 8h16a2 2 0 0 1 2 2v8h-4v4H6v-4H2v-8a2 2 0 0 1 2-2zm4 8v4h8v-4z"/></svg>
        555 372 8815
      </li>
      <li>
        <svg viewBox="0 0 24 24" aria-hidden="true"><path d="M2 5h20v14H2zm2 2v.5l8 5 8-5V7zm0 2.8V17h16V9.8l-8 5z"/></svg>
        daniel@briarwoodmed.com
      </li>
    </ul>

    <address class="address" style="font-style:normal">
      2140 Willow Creek Road<br>
      Juneau, Alaska 99801<br>
      www.briarwoodmed.com
    </address>
  </section>

</div>
</body>
</html>
```